Willow Glow & Laser - Business Banner with Brand Elements

Design:
• We would like to get a creative design for a wide banner that will go outside our medical spa clinic location. We need a designer to make a simple yet colorful and high-quality design layout. We want this banner to be eye-catching and to communicate the services we offer at our business: Laser Hair Removal | Velonix | Lip Filler.

Requirements:
• We would like the banner to include our companies information which is the following:

Logo
“Refresh Your Skin”
Laser Hair Removal | Velonix | Lip Filler
(555) 287-1936
www.WillowGlowLaser.com

Colors:
• Our business colors are orange, a hint of black and white, but mostly peach/orange tones. (Orange: #f78f20 , White: #ffffff)

Fonts:
• Josefins Sans Bold & Lato

Content and images can be located here:
https://files.cloudvaultshare.com/folders/7tQmZ2xVbR9kLpN4sW8yH3cD6fJ1gA0eU?usp=sharing

The following will give you an idea of our brand presentation:
• Our website is: www.WillowGlowLaser.com
• Our Instagram; @willowglowlaser
• Our Facebook: www.socialpagehub.com/willowglowlaser

Target Market(s)
• Women 25 - 45

Industry/Entity Type
• Beauty

```html
<!DOCTYPE html>
<html lang="en">
<head>
<meta charset="utf-8">
<title>Willow Glow &amp; Laser – Storefront Banner</title>
<link rel="stylesheet" href="https://fonts.googleapis.com/css2?family=Lato:wght@400;700;900&display=swap">
<style>
  :root {
    --orange: #f7a541;
    --brand-orange: #f78f20;
    --black: #050505;
    --white: #ffffff;
    --backdrop: #e9e6e2;
    --skin-light: #f3d9cc;
    --skin-mid: #e4b9a6;
    --hair: #6b4a3e;
  }
  * { margin: 0; padding: 0; box-sizing: border-box; }
  html, body {
    width: 1200px; height: 900px; overflow: hidden;
    background: var(--backdrop);
    font-family: "Lato", sans-serif;
  }
  .banner {
    position: absolute; left: 40px; top: 210px;
    width: 1120px; height: 480px;
    background: var(--white);
    overflow: hidden;
    box-shadow: 0 6px 24px rgba(0,0,0,.18);
  }
  .banner__shapes { position: absolute; inset: 0; }
  .headline {
    position: absolute; left: 320px; top: 112px; width: 300px;
    color: var(--white);
    font-weight: 700; font-size: 76px; line-height: 78px;
    text-align center; text-align: center; letter-spacing: -1px;
  }
  .brand {
    position: absolute; right: 40px; top: 46px;
    display: flex; align-items: center; gap: 12px;
  }
  .brand__dot {
    width: 36px; height: 36px; border-radius: 50%;
    background: var(--orange);
  }
  .brand__name {
    color: var(--white); font-weight: 900; font-size: 32px;
    letter-spacing: -0.5px;
  }
  .services {
    position: absolute; right: 40px; top: 128px;
    list-style: none; text-align: right;
  }
  .services__item {
    display: flex; justify-content: flex-end; align-items: center; gap: 14px;
    color: var(--white); font-weight: 700; font-size: 36px; line-height: 50px;
    letter-spacing: -0.5px;
  }
  .services__item::after {
    content: ""; width: 20px; height: 20px; border-radius: 50%;
    background: var(--orange); flex: none;
  }
  .phone {
    position: absolute; right: 316px; top: 400px;
    color: var(--white); font-weight: 400; font-size: 26px; line-height: 40px;
    letter-spacing: 0.5px; white-space: nowrap;
  }
  .website {
    position: absolute; right: 0; top: 398px; width: 300px; height: 44px;
    background: var(--orange);
    color: var(--black); font-weight: 700; font-size: 19px;
    display: flex; align-items: center; justify-content: center;
    letter-spacing: 0.5px; white-space: nowrap;
  }
</style>
</head>
<body>
  <main class="banner">
    <svg class="banner__shapes" width="1120" height="480" viewBox="0 0 1120 480">
      <defs>
        <linearGradient id="portrait-tone" x1="0" y1="0" x2="1" y2="1">
          <stop offset="0" stop-color="#6b4a3e"/>
          <stop offset="0.25" stop-color="#e4b9a6"/>
          <stop offset="0.6" stop-color="#f3d9cc"/>
          <stop offset="1" stop-color="#e4b9a6"/>
        </linearGradient>
      </defs>
      <rect class="panel-dark" x="520" y="0" width="600" height="480" fill="var(--black)"/>
      <path class="bubble-accent" d="M250 60 Q300 10 400 12 L330 90 Z" fill="var(--orange)"/>
      <circle class="circle-ring" cx="470" cy="240" r="232" fill="var(--white)"/>
      <circle class="circle-fill" cx="470" cy="240" r="212" fill="var(--orange)"/>
      <path class="bubble-tail" d="M262 260 L300 340 L322 300 Z" fill="var(--orange)"/>
      <path class="portrait" role="img" aria-label="Portrait photo of a woman with smooth skin, head turned, with dotted lift arrows along the jawline"
        d="M0 0 H230 Q300 140 280 300 Q310 400 420 480 H0 Z" fill="url(#portrait-tone)"/>
    </svg>

    <h1 class="headline">Refresh Your Skin</h1>

    <div class="brand">
      <span class="brand__dot"></span>
      <span class="brand__name">Willow Glow &amp; Laser</span>
    </div>

    <ul class="services">
      <li class="services__item">Laser Hair Removal</li>
      <li class="services__item">Velonix</li>
      <li class="services__item">Lip Filler</li>
    </ul>

    <p class="phone">(555) 287-1936</p>
    <p class="website">www.WillowGlowLaser.com</p>
  </main>
</body>
</html>
```